Flyer-Design für Tonwerk Bündnis Kreis
Zielgruppe
Die Tonwerk Bündnis Kreis ist ein Netzwerk von Musikunternehmen [Labels, Musikproduzenten, Promotionagenturen, Verlag, Tonstudios, Werbetexter, Videoproduzenten].
Wir möchten Musikern und Bands die notwendigen Kontakte vermitteln, damit sie ihr Release bestmöglich am Markt platzieren können. Die Idee ist es, die Musik der Bands schon ab Produktionsbeginn durch uns und unsere Kooperationspartner zu screenen und einen ganzheitlichen Produktions-, Distributions- und Marketingmix anzubieten - oder auch nur Teilbereiche, je nachdem wie es die Band wünscht.
Entsprechend soll das Leistungsspektrum auf dem Flyer angezeigt werden auf der Vorderseite und auf der Rückseite zum Einsenden von Demos aufgefordert werden.
Zielgruppe:
Unsere Leistungen richten sich an unabhängige Bands und Künstler, die in Eigenverantwortlichkeit agieren und professionelle Vermarktungsstrukturen nutzen möchten, wie auch Künstler und Bands, die eine Zusammenarbeit mit Labels anstreben. Über unsere Kooperationspartner können wir diverse Genre abdecken, Pop, Singer/Songwriter, Jazz, Rock, Dance, Folk etc.
Stil des Flyers: passend zum Stil der Webseite www.tonwerk-buendnis-kreis.de
monochrom, s/w ggfls. eine Farbe zur Hervorhebung
Format: druckfertige PDF wird benötigt, sowie PDF zum eMail Versand
Ich benötige die Datei als jpg druckfertig
Aufgabenstellung
Inhalte:
> Logo der Tonwerk Bündnis Kreis
> Claim: Ihr habt die songs – wir das professionelle Netzwerk
> Gitarrenfoto s/w
> Webseite: www.tonwerk-buendnis-kreis.de
Leistungen auf der Vorderseite des Flyers (Plakativ darstellen):
Großhandelslistung wie Kaufhallen Rolf, Pelikon etc.
Weltweite digitale Distribution
Eure Musik bei Wendoro, KBT etc.
Promotion in Radio, Print, Web, TV
Studioproduktion
Mixing/Mastering
Pressetexte
Musikvideoproduktion
Labelcodes / ISRC Codes
CD Pressung
Artwork / CD Cover
EPK
Rückseite des Flyers:
Bewerbung physische Demos:
Tonwerk Bündnis Kreis
Artist & Repertoire
Lindacher Gasse 41
D-67312 Worms
Oder
soundfiles und infopaket (Bio, Bandfotos, Konzerthistorie, Discographie)
über cloudserver (z.B. klangbucht, ablagewerk o.ä )

```html
<!DOCTYPE html>
<html lang="de">
<head>
<meta charset="utf-8">
<title>Tonwerk Bündnis Kreis – Flyer</title>
<link rel="stylesheet" href="https://fonts.googleapis.com/css2?family=Fira+Sans:wght@300;400;700&display=swap">
<style>
  :root {
    --backdrop: #434343;
    --paper: #ffffff;
    --ink: #3a3a3a;
    --ink-soft: #555555;
    --ink-dark: #222222;
    --photo-light: #b9b9b9;
    --photo-mid: #777777;
    --photo-dark: #1c1c1c;
    --headline: #ffffff;
  }
  * { box-sizing: border-box; margin: 0; padding: 0; }
  html, body { width: 1200px; height: 806px; overflow: hidden; }
  body {
    background: var(--backdrop);
    font-family: "Fira Sans", Arial, sans-serif;
    color: var(--ink);
    position: relative;
  }
  .page {
    position: absolute;
    top: 40px;
    width: 510px;
    height: 723px;
    background: var(--paper);
    overflow: hidden;
  }
  .page--front { left: 64px; }
  .page--back { left: 614px; }

  .photo { position: absolute; left: 0; width: 510px; }
  .photo--case {
    top: 93px; height: 537px;
    background:
      radial-gradient(ellipse 45% 40% at 68% 62%, #2a2a2a 0%, #3c3c3c 60%, transparent 100%),
      linear-gradient(180deg, var(--photo-light) 0%, #9c9c9c 25%, var(--photo-mid) 55%, #555 80%, #444 100%);
  }
  .photo--guitar {
    top: 93px; height: 293px;
    background:
      radial-gradient(ellipse 30% 35% at 52% 55%, #8a8a8a 0%, #4a4a4a 55%, transparent 100%),
      linear-gradient(90deg, #3a3a3a 0%, #2b2b2b 40%, var(--photo-dark) 100%);
  }

  .brand-box {
    position: absolute;
    left: 24px; top: 0;
    width: 232px; height: 164px;
    background: var(--paper);
    box-shadow: 2px 2px 6px rgba(0,0,0,.25);
    display: flex; flex-direction: column; align-items: center; justify-content: center; gap: 10px;
  }
  .brand-dot { width: 40px; height: 40px; border-radius: 50%; background: var(--ink); }
  .brand-name {
    font-weight: 700; font-size: 15px; color: var(--ink);
    text-transform: uppercase; letter-spacing: .3px; text-align: center; line-height: 1.15;
  }

  .claim { position: absolute; color: var(--headline); line-height: 1; white-space: nowrap; }
  .claim--intro { left: 24px; top: 287px; font-size: 24px; font-weight: 300; }
  .claim--songs { left: 57px; top: 320px; font-size: 60px; font-weight: 700; letter-spacing: 1px; }
  .claim--lead { left: 136px; top: 530px; font-size: 24px; font-weight: 300; }
  .claim--network { right: 26px; top: 561px; font-size: 64px; font-weight: 700; letter-spacing: 1px; }

  .web {
    position: absolute; left: 0; width: 510px; top: 686px;
    text-align: center; font-size: 13px; font-weight: 300; color: var(--ink);
  }

  .services {
    position: absolute; left: 24px; top: 315px;
    width: 232px; height: 408px;
    background: var(--paper);
    box-shadow: 2px 0 6px rgba(0,0,0,.2);
    list-style: none;
    padding: 26px 10px 0 28px;
    display: flex; flex-direction: column; gap: 7px;
  }
  .services li {
    position: relative; padding-left: 20px;
    font-size: 13.5px; font-weight: 300; line-height: 17.5px; color: var(--ink-soft);
  }
  .services li::before { content: ">"; position: absolute; left: 0; top: 0; font-size: 11px; }

  .submit { position: absolute; left: 308px; width: 195px; }
  .submit--post { top: 466px; }
  .submit--cloud { top: 601px; }
  .submit-icon { position: absolute; left: -30px; top: 4px; }
  .submit-title { font-size: 15px; font-weight: 400; line-height: 19px; color: var(--ink-dark); margin-bottom: 5px; }
  .submit-text { font-size: 11px; font-weight: 300; line-height: 14.6px; color: var(--ink-soft); }
</style>
</head>
<body>
  <section class="page page--front">
    <div class="photo photo--case" role="img" aria-label="Schwarz-weiß Foto: geöffneter Gitarrenkoffer im Gras"></div>
    <div class="brand-box">
      <span class="brand-dot"></span>
      <span class="brand-name">Tonwerk Bündnis Kreis</span>
    </div>
    <p class="claim claim--intro">Ihr habt die</p>
    <p class="claim claim--songs">SONGS</p>
    <p class="claim claim--lead">wir das professionelle</p>
    <p class="claim claim--network">NETZWERK</p>
    <p class="web">www.tonwerk-buendnis-kreis.de</p>
  </section>

  <section class="page page--back">
    <div class="photo photo--guitar" role="img" aria-label="Schwarz-weiß Foto: Hand greift Akkord auf Gitarrenhals mit Kapodaster"></div>
    <div class="brand-box">
      <span class="brand-dot"></span>
      <span class="brand-name">Tonwerk Bündnis Kreis</span>
    </div>
    <ul class="services">
      <li>Großhandelslistung wie Kaufhallen Rolf, Pelikon etc.</li>
      <li>Weltweite digitale Distribution</li>
      <li>Eure Musik bei Wendoro, KBT etc.</li>
      <li>Promotion in Radio, Print, Web, TV</li>
      <li>Studioproduktion</li>
      <li>Mixing/Mastering</li>
      <li>Pressetexte</li>
      <li>Musikvideoproduktion</li>
      <li>Labelcodes / ISRC Codes</li>
      <li>CD Pressung</li>
      <li>Artwork / CD Cover</li>
      <li>EPK</li>
    </ul>

    <div class="submit submit--post">
      <svg class="submit-icon" width="16" height="22" viewBox="0 0 16 22" aria-hidden="true">
        <path d="M8 0C3.6 0 0 3.5 0 7.8 0 13.5 8 22 8 22s8-8.5 8-14.2C16 3.5 12.4 0 8 0z" fill="#333"/>
        <circle cx="8" cy="7.8" r="3" fill="#fff"/>
      </svg>
      <p class="submit-title">Bewerbung physische<br>Demos</p>
      <p class="submit-text">Tonwerk Bündnis Kreis<br>Artist &amp; Repertoire<br>Lindacher Gasse 41<br>D-67312 Worms</p>
    </div>

    <div class="submit submit--cloud">
      <svg class="submit-icon" width="24" height="16" viewBox="0 0 24 16" aria-hidden="true" style="left:-32px;top:8px">
        <path d="M6 16C2.7 16 0 13.6 0 10.6c0-2.7 2.1-4.9 4.9-5.3C5.8 2.2 8.7 0 12 0c3.9 0 7 2.8 7.4 6.4 2.6.4 4.6 2.4 4.6 4.9C24 13.9 21.8 16 19 16z" fill="#333"/>
      </svg>
      <p class="submit-title">Über Cloudserver (zB<br>Klangbucht, Ablagewerk...)</p>
      <p class="submit-text">Soundfiles &amp; Infopaket<br>(Bio, Bandfotos, Konzert-<br>historie, Discographie) an<br>info@tonwerk-buendnis-kreis.de</p>
    </div>
  </section>
</body>
</html>
```